Looking for a person and dog character for dog training school materials

I need two characters to use in my instructional materials for my online dog training program. I’m uploading examples for you of what I’m looking for. I’d like to stay away from details and stay similar to those. Once created, I’ll need the PDFs and printable designed as well. But let’s start with the characters.

Target Market(s)

Dog owners

Industry/Entity Type

Dog training 🐶

Font styles to use
Other font styles liked:
• Not needed

Colors

Designer to choose only greyscale colors for use in the design.

Requirements
Nice to have
• I’ve uploaded samples of what I’m looking for. I’d like basic movements to be shown - dog can sit, down, run, look up, jump etc. Person can point, bend, pet dog, etc. There will be a finite number of positions needed for both
Should not have
• Facial features - details. It will make it too hard to use them in different situations.

```html
<!DOCTYPE html>
<html lang="en">
<head>
<meta charset="utf-8">
<title>Dog Training Characters – Presentation Board</title>
<link rel="stylesheet" href="https://fonts.googleapis.com/css2?family=Oswald:wght@300;400;600&family=Asap+Condensed:wght@300;400;600&family=Roboto+Condensed:wght@400;500&display=swap">
<style>
  :root {
    --ink: #1a1a1a;
    --paper: #ffffff;
    --grey-line: #8a8a8a;
    --red: #9b0a12;
    --teal: #3a7676;
    --blue: #00aeef;
    --orange: #f7941d;
    --green: #00773a;
    --focus-orange: #f26d21;
    --point-blue: #1a7fb0;
    --cream: #fde8cc;
    --silhouette: #1c1c1c;
    --photo-grey: #8c8c8c;
    --photo-green: #6f9a45;
  }
  * { box-sizing: border-box; margin: 0; padding: 0; }
  html, body { width: 1200px; height: 2604px; overflow: hidden; background: var(--paper); }
  body { position: relative; font-family: "Asap Condensed", "Arial Narrow", sans-serif; color: var(--ink); }

  .abs { position: absolute; }

  .character-art { background: var(--silhouette); border-radius: 14px; opacity: .9; }
  .pose-label { font-family: "Oswald", sans-serif; font-weight: 300; font-size: 44px; letter-spacing: .5px; line-height: 1; }

  .troubleshoot { left: 718px; top: 112px; width: 460px; }
  .troubleshoot h2 { font-family: "Oswald", sans-serif; font-weight: 600; font-size: 22px; letter-spacing: 1px; margin-bottom: 28px; }
  .legend-item { position: absolute; left: 0; display: flex; align-items: flex-start; }
  .legend-icon { width: 62px; height: 62px; flex: none; }
  .legend-text { margin-left: 18px; margin-top: -2px; font-size: 17.5px; line-height: 22.5px; font-weight: 300; width: 380px; }

  .pack-photo { left: 718px; top: 782px; width: 428px; height: 270px; border: 2px solid var(--ink);
    background: linear-gradient(135deg, #5a5a5a, #b5b5b5 55%, #7a7a7a); }
  .pack-caption { left: 716px; top: 1060px; font-size: 12.5px; font-weight: 300; }
  .pack-caption b { font-weight: 600; }

  .section-title { left: 68px; font-family: "Oswald", sans-serif; font-weight: 300; font-size: 46px; line-height: 1; }

  .infocard { left: 68px; top: 1200px; width: 1079px; height: 583px; border: 1px solid var(--grey-line); }
  .topic-band { position: absolute; left: 0; top: 0; width: 53px; height: 100%; background: var(--red); }
  .band-label { position: absolute; left: 0; bottom: 14px; width: 100%; writing-mode: vertical-rl; transform: rotate(180deg);
    display: flex; align-items: center; justify-content: flex-start; color: var(--paper);
    font-family: "Roboto Condensed", sans-serif; font-weight: 500; font-size: 34px; letter-spacing: .5px; line-height: 1; }
  .card-title { position: absolute; left: 72px; top: 24px; font-family: "Oswald", sans-serif; font-weight: 600; font-size: 27px; letter-spacing: .2px; }
  .figure-photo { position: absolute; left: 75px; top: 76px; width: 199px; height: 265px; background: linear-gradient(160deg, var(--photo-green), #8bb35a 50%, #5e8a38); }
  .figure-caption { position: absolute; left: 74px; top: 346px; font-family: "Oswald", sans-serif; font-weight: 600; font-size: 17px; }
  .card-body { position: absolute; left: 299px; top: 71px; width: 770px; font-size: 25px; line-height: 38.5px; font-weight: 300; }
  .card-body p { margin-bottom: 12px; }
  .card-body .step-no, .card-body strong { font-weight: 600; }

  .index-bars { left: 70px; top: 1932px; }
  .index-bar { position: absolute; top: 0; width: 52px; height: 580px; }
  .index-bar .band-label { font-size: 31px; bottom: 12px; }
  .bar-leash { left: 0; background: var(--red); }
  .bar-toilet { left: 63px; background: var(--teal); }
  .bar-sit { left: 127px; background: var(--blue); }
  .bar-stand { left: 190px; background: var(--orange); }
  .bar-leave { left: 254px; background: var(--green); }

  .message-panel { left: 505px; top: 1932px; width: 641px; height: 580px; background: var(--orange); color: var(--cream);
    padding: 44px 40px 0 49px; font-weight: 300; font-size: 24px; line-height: 33px; }
  .message-panel p { margin-bottom: 33px; }
</style>
</head>
<body>

  <!-- Character poses -->
  <div class="abs character-art" style="left:60px;top:58px;width:352px;height:236px" role="img" aria-label="Silhouette of a person walking three dogs on leashes"></div>
  <div class="abs pose-label" style="left:445px;top:144px">WALK</div>

  <div class="abs character-art" style="left:74px;top:438px;width:318px;height:230px" role="img" aria-label="Silhouette of a person pointing down at two sitting dogs"></div>
  <div class="abs pose-label" style="left:445px;top:532px">SIT</div>

  <div class="abs character-art" style="left:70px;top:825px;width:296px;height:232px" role="img" aria-label="Silhouette of a person bending over two dogs lying down"></div>
  <div class="abs pose-label" style="left:444px;top:920px">LAY DOWN</div>

  <!-- Troubleshoot legend -->
  <section class="abs troubleshoot">
    <h2>TROUBLESHOOT</h2>

    <div class="legend-item" style="top:56px">
      <svg class="legend-icon" viewBox="0 0 62 62"><circle cx="31" cy="31" r="31" fill="var(--silhouette)"/>
        <ellipse cx="31" cy="31" rx="9" ry="7" fill="#fff"/><circle cx="20" cy="22" r="4" fill="#fff"/><circle cx="27" cy="16" r="4" fill="#fff"/><circle cx="35" cy="16" r="4" fill="#fff"/><circle cx="42" cy="22" r="4" fill="#fff"/>
        <text x="31" y="52" text-anchor="middle" font-size="9" fill="#fff" font-family="Asap Condensed, sans-serif">TIP</text></svg>
      <p class="legend-text">This icon draws your attention to ways to save time, money, energy, and your sanity.</p>
    </div>

    <div class="legend-item" style="top:158px">
      <svg class="legend-icon" viewBox="0 0 62 62"><circle cx="31" cy="31" r="31" fill="var(--red)"/>
        <rect x="28" y="10" width="6" height="22" rx="3" fill="#fff"/><circle cx="31" cy="38" r="3.2" fill="#fff"/>
        <text x="31" y="53" text-anchor="middle" font-size="9" fill="#fff" font-family="Asap Condensed, sans-serif">DANGER</text></svg>
      <p class="legend-text">This icon raises a red flag; your safety or your dog’s may be at risk. It also tells you about the don’ts of dog training. Proceed at your own risk!</p>
    </div>

    <div class="legend-item" style="top:260px">
      <svg class="legend-icon" viewBox="0 0 62 62"><circle cx="31" cy="31" r="31" fill="var(--point-blue)"/>
        <ellipse cx="31" cy="28" rx="15" ry="8" fill="none" stroke="#fff" stroke-width="2.5"/><ellipse cx="31" cy="33" rx="15" ry="6" fill="none" stroke="#fff" stroke-width="2"/>
        <text x="31" y="53" text-anchor="middle" font-size="9" fill="#fff" font-family="Asap Condensed, sans-serif">POINT</text></svg>
      <p class="legend-text">This icon directs you to information that’s important to remember – key points that you want to focus on.</p>
    </div>

    <div class="legend-item" style="top:358px">
      <svg class="legend-icon" viewBox="0 0 62 62"><circle cx="31" cy="31" r="31" fill="var(--focus-orange)"/>
        <circle cx="19" cy="27" r="5" fill="none" stroke="#fff" stroke-width="2.5"/><rect x="24" y="24" width="24" height="6" fill="#fff"/>
        <text x="31" y="50" text-anchor="middle" font-size="9" fill="#fff" font-family="Asap Condensed, sans-serif">FOCUS</text></svg>
      <p class="legend-text">This icon highlights in-depth information that isn’t critical for you to know but that can enhance your knowledge of dog training and make you a better teacher.</p>
    </div>

    <div class="legend-item" style="top:461px">
      <svg class="legend-icon" viewBox="0 0 62 62"><circle cx="31" cy="31" r="31" fill="var(--green)"/>
        <rect x="19" y="25" width="24" height="7" fill="#fff"/><circle cx="18" cy="24" r="4.5" fill="#fff"/><circle cx="18" cy="33" r="4.5" fill="#fff"/><circle cx="44" cy="24" r="4.5" fill="#fff"/><circle cx="44" cy="33" r="4.5" fill="#fff"/>
        <text x="31" y="53" text-anchor="middle" font-size="9" fill="#fff" font-family="Asap Condensed, sans-serif">RESULT</text></svg>
      <p class="legend-text">This icon points out stories of successful dog training techniques and strategies.</p>
    </div>
  </section>

  <div class="abs pack-photo" role="img" aria-label="Black and white photo of a puppy touching noses with a woman crouching on the grass"></div>
  <p class="abs pack-caption"><b>Figure 2-2:</b> A dog enjoying physical contact with a person, a typical pack drive behavior</p>

  <!-- Infocard idea -->
  <h2 class="abs section-title" style="top:1130px">Infocard Idea</h2>

  <article class="abs infocard">
    <div class="topic-band"><span class="band-label">LEASH TRAINING</span></div>
    <h3 class="card-title">TEACHING COMPANION TO RESPECT THE LEASH</h3>
    <div class="figure-photo" role="img" aria-label="Photo of an open hand holding a purple leash loop over the thumb, grass behind"></div>
    <p class="figure-caption">FIGURE 1-1</p>
    <div class="card-body">
      <p>Take companion to an area that’s familiar to him and where there are no distractions your backyard or a quiet street are good places.</p>
      <p><span class="step-no">1.</span> Put the loop of the leash over the thumb of your left hand and make a fist around the leash. <strong>Figure 1-1 shows you how this should look.</strong></p>
      <p><span class="step-no">2.</span> Place your right hand directly under your left hand and make a fist around the leash. Hold the leash in both hands as though it were a baseball bat. Plant both hands firmly against your belt buckle.</p>
      <p><span class="step-no">3.</span> Say “Let’s Go,” or any other command you choose, and start walking.</p>
      <p><span class="step-no">4.</span> Just before Buddy gets to the end of the leash, say “Let’s Go.” Without turning your head to look at him, make an about-turn to your right and walk in the opposite direction.</p>
    </div>
  </article>

  <!-- Topic indexing -->
  <h2 class="abs section-title" style="top:1855px">Infocard Topic Indexing</h2>

  <div class="abs index-bars">
    <div class="index-bar bar-leash"><span class="band-label">LEASH TRAINING</span></div>
    <div class="index-bar bar-toilet"><span class="band-label">TOILET TRAINING</span></div>
    <div class="index-bar bar-sit"><span class="band-label">FUNDAMENTALS: SIT</span></div>
    <div class="index-bar bar-stand"><span class="band-label">FUNDAMENTALS: STAND</span></div>
    <div class="index-bar bar-leave"><span class="band-label">FUNDAMENTALS: LEAVE</span></div>
  </div>

  <div class="abs message-panel">
    <p>Hello Again.<br>We can do whatever needed for your project.<br>PDF for prints, ePDF’s, training cards and even social media advertisements and posts if needed. If you can brief us about a specific subject, we would be more than happy to design it for you.</p>
    <p>Our project manager tried to contact you via messages section in briefboard but unable to receive any answers.</p>
    <p>So if it suits you, we can talk more detailed from there.<br>Thank you.</p>
  </div>

</body>
</html>
```